Business Card Design - Crisp & Clean

Looking for a new clean and crisp business card design. Design must incorporate our corporate colors (see attached style sheet). We're a pretty fun loving group who likes to keep it light while still portraying a professional image. Card should incorporate both our logo and our mascot (see attachment). Card should be double sided and should have room for our social media - Gleamrow, Brisk Hub and Zumbly on the back. Font selections do not have to match the style guide.

```html
<!DOCTYPE html>
<html lang="en">
<head>
<meta charset="utf-8">
<title>LumoraHR Business Cards</title>
<link href="https://fonts.googleapis.com/css2?family=Titillium+Web:wght@300;400;600;700&display=swap" rel="stylesheet">
<style>
  :root {
    --backdrop: #e4e4e2;
    --card: #f7f7f5;
    --ink: #2b2b2b;
    --ink-soft: #555555;
    --orange: #e9581f;
    --yellow: #f4bd2a;
    --accent-warm: #f6c928;
    --art-light: #e9e4da;
    --art-dark: #c9c2b4;
    --rule: #6a6a6a;
  }
  * { box-sizing: border-box; margin: 0; padding: 0; }
  html, body {
    width: 1200px; height: 1000px; overflow: hidden;
    background: var(--backdrop);
    font-family: "Titillium Web", sans-serif;
    color: var(--ink);
  }
  .card {
    position: absolute; width: 640px; height: 366px;
    background: var(--card);
    box-shadow: 0 4px 14px rgba(0,0,0,.12);
    overflow: hidden;
  }
  .card--brand { left: 280px; top: 70px; }
  .card--contact { left: 280px; top: 520px; }

  .edge-strip {
    position: absolute; right: 0; top: 0; bottom: 0; width: 8px;
    background: var(--orange);
  }

  .wordmark { position: absolute; display: flex; align-items: center; gap: 10px; }
  .wordmark__dot { width: 22px; height: 22px; border-radius: 50%; background: var(--yellow); }
  .wordmark__name { font-weight: 700; font-size: 34px; line-height: 1; color: var(--ink); letter-spacing: .5px; }
  .wordmark__tagline {
    position: absolute; font-size: 9px; font-weight: 700; letter-spacing: .6px;
    text-transform: uppercase; color: var(--ink);
  }

  .card--brand .wordmark { left: 70px; top: 160px; }
  .card--brand .wordmark__tagline { left: 102px; top: 198px; }

  .art {
    position: absolute; border-radius: 46% 46% 30% 30%;
    background: linear-gradient(160deg, var(--accent-warm) 0%, var(--art-light) 45%, var(--art-dark) 100%);
  }
  .card--brand .art { right: 60px; top: 60px; width: 210px; height: 250px; }
  .card--contact .art { right: 40px; top: 24px; width: 110px; height: 130px; }

  .icon-block { position: absolute; left: 34px; top: 14px; width: 46px; height: 118px; }
  .icon-block__rule { position: absolute; left: 0; width: 46px; height: 1px; background: var(--rule); }
  .icon-block__rule--top { top: 0; }
  .icon-block__rule--bottom { bottom: 0; }
  .icon-block__bulb {
    position: absolute; left: 6px; top: 36px; width: 34px; height: 46px;
    border-radius: 50% 50% 40% 40%;
    background: linear-gradient(180deg, var(--accent-warm), #e2a914);
  }

  .person { position: absolute; left: 100px; top: 22px; }
  .person__name { font-size: 40px; font-weight: 300; letter-spacing: 1px; line-height: 1.1; }
  .person__role {
    font-size: 24px; font-weight: 400; color: var(--ink-soft); line-height: 1.2;
    border-bottom: 1.5px solid var(--rule); padding-bottom: 2px; display: inline-block;
  }

  .band {
    position: absolute; height: 34px; display: flex; align-items: center;
    padding-left: 16px; font-size: 19px; font-weight: 400; white-space: nowrap;
  }
  .band--phone { left: 40px; top: 148px; width: 330px; background: var(--orange); color: #fff; }
  .band--email { left: 40px; top: 188px; width: 390px; background: var(--yellow); color: var(--ink); }
  .band--slogan { left: 320px; bottom: 24px; width: 320px; background: var(--yellow); color: var(--ink); }

  .card--contact .wordmark { left: 60px; top: 262px; }
  .card--contact .wordmark__tagline { left: 92px; top: 300px; }
</style>
</head>
<body>

<section class="card card--brand">
  <div class="wordmark">
    <span class="wordmark__dot"></span>
    <span class="wordmark__name">LumoraHR</span>
  </div>
  <span class="wordmark__tagline">HR Process Management Solutions</span>
  <div class="art" role="img" aria-label="Mascot illustration"></div>
  <div class="edge-strip"></div>
</section>

<section class="card card--contact">
  <div class="icon-block">
    <span class="icon-block__rule icon-block__rule--top"></span>
    <div class="icon-block__bulb" role="img" aria-label="Small icon"></div>
    <span class="icon-block__rule icon-block__rule--bottom"></span>
  </div>
  <div class="person">
    <h1 class="person__name">DANA WHITFIELD</h1>
    <p class="person__role">marketing wizard</p>
  </div>
  <div class="band band--phone">Mobile: 555.010.2468</div>
  <div class="band band--email">dana@lumorahr.com</div>
  <div class="art" role="img" aria-label="Small mascot illustration"></div>
  <div class="wordmark">
    <span class="wordmark__dot"></span>
    <span class="wordmark__name">LumoraHR</span>
  </div>
  <span class="wordmark__tagline">HR Process Management Solutions</span>
  <div class="band band--slogan">LumoraHR Processing Solutions</div>
</section>

</body>
</html>
```